Loftvane.ca Your Canadian Source for all your mortgage needs.

I need to get a fresh look on my current website. It is not currently a Wordpress site and i need to build a whole new site that i can do my editing in using Wordpress.
I need it built in a mobile or responsive theme.
There will be a secured application page which is critical.
I have 3 books written so i want to be able to have advertising spaces for promoting them and a landing page ( I can build my own landing pages)
I need the frame work of a professional theme with easy editing capabilities.
I have my own LOGOs which i would continue to use. The current site can be reviewed at www.loftvane.ca.
The front page could have a young couple near a nice house, open to suggestions.
I don't need a blog post to update but if it was on the sides of the pages I could use it. Something like a "Latest News" section.
I would like to have a Main page, Application Page, Resource page, Contact page, Calculator Page, a questions and answer page. Theses can be populated with the current information or I can add latter.
I want the main page to be a mini sales page so I can link to Posts on First Time Home Buyers, Refinance Options, Second Home or New purchase options.
I provide mortgages for people across Canada so i want the Canadian Flag incorporated
I like the colors to work with the logo colors on the current site

Target Market(s)

Canadian Mortgage Clients

Font styles to use
Sans Serif

Colors
3277b5
cadf82

Requirements
Must have
• Must work in a Wordpress Theme
• Please see Project description for more details
Nice to have
• Space to add banner ads for my books. I have 3 books written

```html
<!DOCTYPE html>
<html lang="en">
<head>
<meta charset="utf-8">
<title>Loftvane.ca — Mortgages Across Canada</title>
<link href="https://fonts.googleapis.com/css2?family=Open+Sans:wght@400;600;700&family=Oswald:wght@500;600&display=swap" rel="stylesheet">
<style>
:root{
  --blue:#3277b5;
  --blue-dark:#2a64a0;
  --green:#8db43a;
  --green-light:#cadf82;
  --ink:#333;
  --muted:#666;
  --red:#d0312d;
  --grey-bg:#f1f1f1;
  --rule:#dcdcdc;
  --white:#fff;
}
*{box-sizing:border-box;margin:0;padding:0}
html,body{width:1200px;height:2312px;overflow:hidden}
body{font-family:"Open Sans",Arial,sans-serif;color:var(--ink);background:var(--white);position:relative}
.site-header{height:112px;position:relative;background:var(--white)}
.topbar{position:absolute;top:8px;left:160px;right:160px;display:flex;justify-content:space-between;font-size:12px;color:var(--muted)}
.top-social{display:flex;gap:8px}
.top-social span{width:14px;height:14px;background:var(--blue);display:block}
.brand{position:absolute;left:160px;top:34px;display:flex;align-items:center;gap:12px}
.brand-mark{width:30px;height:30px;border-radius:50%;background:var(--green)}
.brand-name{font-size:34px;font-weight:700;color:var(--blue);letter-spacing:1px}
.main-nav{position:absolute;right:160px;top:60px;display:flex;gap:38px;font-size:14px}
.main-nav a{color:var(--muted);text-decoration:none}
.main-nav a.active{color:var(--blue);font-weight:600}
.hero{position:absolute;top:112px;left:0;width:1200px;height:568px;background:linear-gradient(180deg,#9cc6ea 0%,#d6e6f1 45%,#7b9b4c 82%,#5b7d33 100%)}
.hero-tagline{position:absolute;right:0;top:440px;width:640px;height:128px;background:rgba(20,30,40,.65);padding:20px 60px 0 0;text-align:right;font-family:"Oswald",Arial,sans-serif;font-weight:600;color:var(--white);font-size:38px;line-height:44px;text-transform:uppercase}
.why{position:absolute;top:680px;left:0;width:1200px;height:600px;background:var(--grey-bg)}
.why h2{position:absolute;left:160px;top:60px;font-size:36px;font-weight:700;color:var(--ink)}
.why h2 em{font-style:normal;color:var(--blue)}
.why-copy{position:absolute;left:160px;top:130px;width:540px;font-size:12px;line-height:18px;color:var(--muted)}
.why-copy p{margin-bottom:14px}
.why-copy .offer{color:var(--red);font-weight:700}
.book-ad{position:absolute;left:740px;top:60px;width:290px;height:480px;background:linear-gradient(180deg,#f4f4f4 0%,#e1ecf5 55%,#9fb98a 100%);border:1px solid var(--rule)}
.features{position:absolute;top:1320px;left:160px;width:880px;display:flex;justify-content:space-between}
.feature{width:272px}
.feature-img{height:152px;background:linear-gradient(135deg,#e9eef2,#c7d3dc);border:1px solid var(--rule)}
.feature-btn{height:40px;background:var(--blue);color:var(--white);font-size:15px;font-weight:600;text-align:center;line-height:40px;text-transform:uppercase}
.news{position:absolute;top:1620px;left:0;width:1200px;height:420px;background:#f7f7f7}
.news h2{position:absolute;left:160px;top:50px;font-size:36px;font-weight:700;color:var(--blue)}
.news h2 em{font-style:normal;color:var(--ink)}
.news-list{position:absolute;left:160px;top:125px;width:440px;list-style:none}
.news-list li{display:flex;gap:18px;align-items:flex-start;margin-bottom:24px;font-size:12px;line-height:18px;color:var(--muted)}
.news-num{flex:0 0 40px;height:40px;border-radius:50%;background:var(--green);color:var(--white);font-weight:700;font-size:14px;display:flex;align-items:center;justify-content:center}
.view-all{position:absolute;left:160px;top:370px;width:80px;height:26px;background:var(--blue);color:var(--white);font-size:11px;font-weight:600;text-align:center;line-height:26px}
.news-img{position:absolute;left:680px;top:60px;width:360px;height:320px;background:linear-gradient(135deg,#f4f1ec 0%,#d8c6a6 55%,#8fb6d6 100%)}
.site-footer{position:absolute;top:2080px;left:0;width:1200px;height:232px;background:var(--blue);color:var(--white)}
.footer-links{position:absolute;top:34px;font-size:11px;line-height:22px;list-style:none}
.footer-links.col-1{left:160px}
.footer-links.col-2{left:380px}
.footer-title{position:absolute;top:30px;font-size:18px;font-weight:600}
.follow{left:610px}
.follow-icons{position:absolute;left:610px;top:70px;display:flex;gap:10px}
.follow-icons span{width:32px;height:32px;border-radius:50%;background:var(--green);display:block}
.signup{left:840px}
.signup-form{position:absolute;left:840px;top:70px;width:200px;font-size:11px}
.signup-form label{display:flex;justify-content:space-between;align-items:center;margin-bottom:8px}
.signup-form .field{width:120px;height:18px;background:var(--white)}
.signup-btn{margin-left:80px;width:70px;height:20px;background:var(--green);color:var(--white);font-size:10px;font-weight:700;text-align:center;line-height:20px}
.copyright{position:absolute;bottom:0;left:0;width:1200px;height:34px;background:var(--blue-dark);text-align:center;font-size:10px;line-height:34px;letter-spacing:.5px}
</style>
</head>
<body>
<header class="site-header">
  <div class="topbar"><span>905-555-0142</span><div class="top-social"><span></span><span></span><span></span></div></div>
  <div class="brand"><span class="brand-mark"></span><span class="brand-name">Loftvane</span></div>
  <nav class="main-nav">
    <a class="active" href="#">Main</a><a href="#">Application</a><a href="#">Resource</a><a href="#">Contact</a><a href="#">Calculator</a><a href="#">Apply Now</a>
  </nav>
</header>

<section class="hero" role="img" aria-label="Smiling young couple in front of a brick house with a green lawn under a blue sky">
  <div class="hero-tagline">Customize your mortgage<br>Save thousands of dollars</div>
</section>

<section class="why">
  <h2><em>Why</em> Choose Us ?</h2>
  <div class="why-copy">
    <p>Professional representation for you and your family is vital. Navigating rates on your biggest investment is not easy. Allowing us to work for you will help you find the right path.</p>
    <p>Is your current home financing plan working for you? Our team compares lenders across Canada and builds a plan that fits your goals, your budget and your timeline. Switching later is simple and free.</p>
    <p>Planning to buy your first home or renew your existing term? Talk to us before you sign.</p>
    <p>We will help you save thousands over the life of your loan with better rates, smarter terms and honest advice at every step.</p>
    <p>Because we work with many lenders, we shop the market for you and bring the best options back to your table.</p>
    <p class="offer">NO FEE to talk to you about rates. We work for the banks and lenders so you get expert help at no cost to you.</p>
    <p>Call Today.</p>
  </div>
  <div class="book-ad" role="img" aria-label="Advertisement for a home buying book, with a family in front of a house"></div>
</section>

<section class="features">
  <div class="feature"><div class="feature-img" role="img" aria-label="Hand on a computer mouse beside a keyboard"></div><div class="feature-btn">Apply Online Now</div></div>
  <div class="feature"><div class="feature-img" role="img" aria-label="Stacked coins with a small model house"></div><div class="feature-btn">Save Thousands</div></div>
  <div class="feature"><div class="feature-img" role="img" aria-label="Calculator and pen on financial papers"></div><div class="feature-btn">Mortgage Calculator</div></div>
</section>

<section class="news">
  <h2>Latest <em>News</em></h2>
  <ul class="news-list">
    <li><span class="news-num">01</span><span>Current fixed rates hold steady this month while lenders add new first time buyer offers across Canada.</span></li>
    <li><span class="news-num">02</span><span>New rules for refinance options mean more choice for owners planning a renovation or debt payoff.</span></li>
    <li><span class="news-num">03</span><span>Thinking of a second home or cottage? Learn how down payment rules differ for each property type.</span></li>
  </ul>
  <div class="view-all">VIEW ALL</div>
  <div class="news-img" role="img" aria-label="Hands holding a small model house with a red roof"></div>
</section>

<footer class="site-footer">
  <ul class="footer-links col-1"><li>HOME</li><li>ABOUT US</li><li>CONTACT</li><li>F.A.Q.</li><li>DOCUMENT LIBRARY</li></ul>
  <ul class="footer-links col-2"><li>CORPORATE AFFILIATES</li><li>MORTGAGE CALCULATORS</li><li>BOOK SALES</li><li>APPLY ONLINE</li><li>PRIVACY POLICY</li></ul>
  <div class="footer-title follow">Follow us</div>
  <div class="follow-icons"><span></span><span></span><span></span></div>
  <div class="footer-title signup">Newsletter Signup</div>
  <div class="signup-form">
    <label>Name <span class="field"></span></label>
    <label>Email <span class="field"></span></label>
    <div class="signup-btn">SUBMIT</div>
  </div>
  <div class="copyright">COPYRIGHT © 2024 LOFTVANE.CA ALL RIGHTS RESERVED</div>
</footer>
</body>
</html>
```